Business Card Design for Miss Poppy's Soak Parlour

Name: Miss Poppy's Soak Parlour. Maker of bath bombs, bath salts.

Card details:

Donna Pickett
1.702.555.0143
Silverpine Nevada
dpickett47@mailpost.example

"Bath bombs, bath salts and more..."

A picture of an old-fashioned bathtub (with claw feet) filled with bath bombs.

Colors include: Lavender, Pink, Turquois, Light Blue. Can you make the overall design look old fashioned.

```html
<!DOCTYPE html>
<html lang="en">
<head>
<meta charset="utf-8">
<title>Miss Poppy's Soak Parlour – Business Card</title>
<link rel="stylesheet" href="https://fonts.googleapis.com/css2?family=Roboto:wght@400;500;700&display=swap">
<style>
  :root {
    --page-bg: #efe6d2;
    --card-bg: #0f0e11;
    --accent-pink: #e8138c;
    --tub-pink: #f0a3c9;
    --tub-pink-light: #f6c2dc;
    --text-white: #ffffff;
  }
  html, body {
    margin: 0;
    padding: 0;
    width: 1200px;
    height: 900px;
    overflow: hidden;
    background: var(--page-bg);
    font-family: "Roboto", Arial, sans-serif;
  }
  .canvas {
    position: relative;
    width: 1200px;
    height: 900px;
  }
  .business-card {
    position: absolute;
    left: 100px;
    top: 164px;
    width: 1000px;
    height: 572px;
    background: var(--card-bg);
  }
  .brand-artwork {
    position: absolute;
    left: 338px;
    top: 89px;
    width: 276px;
    height: 103px;
    border-radius: 40px 40px 50px 50px;
    background: linear-gradient(180deg, var(--tub-pink-light) 0%, var(--tub-pink) 100%);
  }
  .brand-name {
    position: absolute;
    left: 0;
    width: 960px;
    top: 202px;
    margin: 0;
    line-height: 44px;
    text-align: center;
    font-size: 38px;
    font-weight: 700;
    color: var(--accent-pink);
    white-space: nowrap;
  }
  .tagline {
    position: absolute;
    left: 0;
    width: 960px;
    top: 253px;
    margin: 0;
    line-height: 32px;
    text-align: center;
    font-size: 26px;
    font-weight: 500;
    color: var(--text-white);
    white-space: nowrap;
  }
  .person-name {
    position: absolute;
    left: 96px;
    top: 392px;
    margin: 0;
    line-height: 54px;
    font-size: 46px;
    font-weight: 700;
    color: var(--accent-pink);
    white-space: nowrap;
  }
  .divider {
    position: absolute;
    left: 466px;
    top: 398px;
    width: 4px;
    height: 132px;
    background: var(--accent-pink);
  }
  .contact-list {
    position: absolute;
    left: 554px;
    top: 396px;
    margin: 0;
    padding: 0;
    list-style: none;
  }
  .contact-item {
    display: flex;
    align-items: center;
    height: 40px;
    font-size: 29px;
    color: var(--text-white);
    white-space: nowrap;
  }
  .contact-item--location {
    color: var(--accent-pink);
  }
  .contact-icon {
    width: 22px;
    height: 22px;
    margin-right: 10px;
    flex: none;
  }
</style>
</head>
<body>
<main class="canvas">
  <section class="business-card">
    <div class="brand-artwork" role="img" aria-label="Illustration of a pink clawfoot bathtub"></div>
    <h1 class="brand-name">Miss Poppy's Soak Parlour</h1>
    <p class="tagline">"Bath bombs, bath salts and more...</p>

    <h2 class="person-name">Donna Pickett</h2>
    <div class="divider"></div>

    <ul class="contact-list">
      <li class="contact-item">
        <svg class="contact-icon" viewBox="0 0 24 24" aria-hidden="true">
          <path fill="#ffffff" d="M6.6 10.8c1.4 2.8 3.8 5.1 6.6 6.6l2.2-2.2c.3-.3.7-.4 1-.2 1.1.4 2.3.6 3.6.6.6 0 1 .4 1 1V20c0 .6-.4 1-1 1C10.6 21 3 13.4 3 4c0-.6.4-1 1-1h3.5c.6 0 1 .4 1 1 0 1.3.2 2.5.6 3.6.1.3 0 .7-.2 1z"/>
        </svg>
        <span>1.702.555.0143</span>
      </li>
      <li class="contact-item contact-item--location">
        <svg class="contact-icon" viewBox="0 0 24 24" aria-hidden="true">
          <path fill="#e8138c" d="M12 2C8.1 2 5 5.1 5 9c0 5.2 7 13 7 13s7-7.8 7-13c0-3.9-3.1-7-7-7zm0 9.5a2.5 2.5 0 1 1 0-5 2.5 2.5 0 0 1 0 5z"/>
        </svg>
        <span>Silverpine Nevada</span>
      </li>
      <li class="contact-item">
        <svg class="contact-icon" viewBox="0 0 24 24" aria-hidden="true">
          <path fill="#ffffff" d="M2 5h20v14H2z"/>
          <path fill="none" stroke="#0f0e11" stroke-width="1.6" d="M2 5l10 7 10-7"/>
        </svg>
        <span>dpickett47@mailpost.example</span>
      </li>
    </ul>
  </section>
</main>
</body>
</html>
```